Profesional personal website needs design and business card

I need a business card with my professional name as a logo "Marlo Vitality" for my business. I am a Wellness Coach, consultant and trainer. So it should be professional, wellness oriented and modern.

Target Market(s)

Private clients, governments, corporations. Luxury and high market.

Industry/Entity Type

Health And Wellness

Contact Information for Business Card

Marlo Vitality should be the logo

Colors

Designer to choose colors to be used in the design.

Requirements
Must have
• Marlo Vitality
• Name: Tomás Arribal
• Wellness Coach, Consultant & Trainer.
• Website: www.marlovitality.example
• Phone:
• Spain (+34) 612 480 397
• (USA) +1 (555) 318 2046
Nice to have
• The most important is the design of "Marlo Vitality", as this is going to be my personal brand logo. It should be professional, wellness, high end and actual.
Should not have
• no golds, no baroque style..

```html
<!DOCTYPE html>
<html lang="en">
<head>
<meta charset="utf-8">
<title>Marlo Vitality — Business Card</title>
<link rel="stylesheet" href="https://fonts.googleapis.com/css2?family=Montserrat:wght@400;500;700&display=swap">
<style>
  :root {
    --forest: #1a3319;
    --leaf: #6cc04a;
    --paper: #ffffff;
    --backdrop: #eef1ec;
    --ink: #1a3319;
  }
  * { box-sizing: border-box; margin: 0; padding: 0; }
  html, body {
    width: 1200px;
    height: 1200px;
    overflow: hidden;
  }
  body {
    position: relative;
    background: var(--backdrop);
    font-family: "Montserrat", sans-serif;
    color: var(--ink);
  }
  .card {
    position: absolute;
    left: 190px;
    width: 820px;
    height: 522px;
    border-radius: 40px;
    overflow: hidden;
    box-shadow: 0 4px 14px rgba(0, 0, 0, 0.18);
  }

  /* Back side */
  .card--back {
    top: 40px;
    background: var(--forest);
    display: flex;
    align-items: center;
    justify-content: center;
  }
  .brand {
    display: flex;
    align-items: center;
    gap: 16px;
  }
  .brand__name {
    font-weight: 500;
    text-transform: uppercase;
    letter-spacing: 0.08em;
    line-height: 1.05;
  }
  .brand__dot {
    border-radius: 50%;
    background: var(--leaf);
    flex: none;
  }
  .card--back .brand__name { color: var(--paper); font-size: 60px; }
  .card--back .brand__dot { width: 34px; height: 34px; }

  /* Front side */
  .card--front {
    top: 618px;
    background: var(--paper);
  }
  .tab {
    position: absolute;
    top: 146px;
    width: 42px;
    height: 228px;
  }
  .tab--left {
    left: 0;
    background: var(--forest);
    border-radius: 0 42px 42px 0;
  }
  .tab--right {
    right: 0;
    background: var(--leaf);
    border-radius: 42px 0 0 42px;
  }
  .card--front .brand {
    position: absolute;
    left: 127px;
    top: 261px;
    transform: translateY(-50%);
    gap: 10px;
  }
  .card--front .brand__name { color: var(--forest); font-size: 32px; }
  .card--front .brand__dot { width: 18px; height: 18px; }

  .divider {
    position: absolute;
    left: 410px;
    top: 146px;
    width: 3px;
    height: 228px;
    background: linear-gradient(to bottom, var(--forest) 0 50%, var(--leaf) 50% 100%);
  }
  .details {
    position: absolute;
    left: 425px;
    top: 140px;
  }
  .details__name {
    font-size: 31px;
    font-weight: 700;
    line-height: 1.2;
    margin-bottom: 6px;
  }
  .details__role {
    font-size: 22px;
    font-weight: 400;
    line-height: 1.42;
  }
  .details__contact {
    list-style: none;
    margin-top: 26px;
    font-size: 22px;
    font-weight: 400;
    line-height: 1.85;
  }
</style>
</head>
<body>
  <section class="card card--back" aria-label="Card back">
    <div class="brand">
      <span class="brand__name">Marlo<br>Vitality</span>
      <span class="brand__dot"></span>
    </div>
  </section>

  <section class="card card--front" aria-label="Card front">
    <span class="tab tab--left"></span>
    <span class="tab tab--right"></span>

    <div class="brand">
      <span class="brand__name">Marlo<br>Vitality</span>
      <span class="brand__dot"></span>
    </div>

    <span class="divider"></span>

    <div class="details">
      <h1 class="details__name">Tomás Arribal</h1>
      <p class="details__role">Wellness Coach<br>Consultant &amp; Trainer</p>
      <ul class="details__contact">
        <li>Spain (+34) 612 480 397</li>
        <li>USA +1 (555) 318 2046</li>
        <li>www.marlovitality.example</li>
      </ul>
    </div>
  </section>
</body>
</html>
```